Kinward Harbor Center
Stationary and Business Cards
Kinward Harbor Center -
Creative Brief
Bright & Fun-filled
Marisol Thackery
48 Alder Lane Morristown, NJ 07931
marisol.thackery@alderlanehub.org
www.alderlanehub.org

```html
<!DOCTYPE html>
<html lang="en">
<head>
<meta charset="utf-8">
<title>Kinward Harbor Center – Stationery</title>
<link href="https://fonts.googleapis.com/css2?family=Cinzel:wght@600&family=Open+Sans:wght@400;600&display=swap" rel="stylesheet">
<style>
  :root {
    --backdrop: #a7a8aa;
    --paper: #ffffff;
    --navy: #2d4d84;
    --blue: #3f6fb0;
    --orange: #e8832a;
    --ink: #4a4f57;
    --muted: #7d838c;
    --faint: #e8edf4;
  }
  * { margin: 0; padding: 0; box-sizing: border-box; }
  html, body { width: 1200px; height: 626px; overflow: hidden; }
  body { background: var(--backdrop); font-family: "Open Sans", sans-serif; color: var(--ink); position: relative; }

  .sheet { position: absolute; background: var(--paper); box-shadow: 0 1px 3px rgba(0,0,0,.25); }

  .brand { display: flex; flex-direction: column; align-items: center; gap: 3px; }
  .brand-dot { width: 14px; height: 14px; border-radius: 50%; background: var(--blue); }
  .brand-name { font-family: "Cinzel", serif; font-weight: 600; color: var(--navy); letter-spacing: .08em; text-transform: uppercase; white-space: nowrap; }
  .brand-tag { font-size: 4px; color: var(--muted); letter-spacing: .1em; text-transform: uppercase; }

  /* Business card */
  .card { left: 24px; top: 312px; width: 197px; height: 187px; overflow: hidden; }
  .card .brand { margin-top: 30px; }
  .card .brand-name { font-size: 7px; }
  .card-band { position: absolute; left: 0; right: 0; bottom: 0; height: 72px; background: linear-gradient(180deg, var(--blue), var(--navy)); color: #fff; padding: 12px 10px; }
  .card-name { font-size: 7.5px; font-weight: 600; text-align: right; }
  .card-info { font-size: 4.3px; line-height: 1.6; margin-top: 12px; text-align: center; opacity: .9; }

  /* Letterhead */
  .letterhead { left: 233px; top: 29px; width: 374px; height: 571px; }
  .letterhead .brand { margin-top: 26px; }
  .letterhead .brand-name { font-size: 7px; }
  .watermark { position: absolute; left: 97px; top: 160px; width: 180px; height: 180px; border-radius: 50%; background: var(--faint); }
  .letter-foot { position: absolute; left: 0; right: 0; bottom: 26px; text-align: center; }
  .web { font-size: 5px; color: var(--orange); }
  .contact-line { font-size: 4.3px; color: var(--muted); margin-top: 6px; }

  /* Envelopes */
  .env-back { left: 643px; top: 240px; width: 521px; height: 156px; overflow: hidden; }
  .env-back svg { position: absolute; inset: 0; }
  .env-front { left: 643px; top: 432px; width: 521px; height: 168px; }
  .env-front .letter-foot { bottom: 30px; }
</style>
</head>
<body>

  <section class="sheet card" aria-label="Business card">
    <div class="brand">
      <span class="brand-dot"></span>
      <span class="brand-name">Kinward Harbor Center</span>
      <span class="brand-tag">Building Stronger Families Together</span>
    </div>
    <div class="card-band">
      <p class="card-name">Marisol Thackery</p>
      <p class="card-info">P: 973-555-0142 | E: marisol.thackery@alderlanehub.org<br>48 Alder Lane Morristown, NJ 07931</p>
    </div>
  </section>

  <section class="sheet letterhead" aria-label="Letterhead">
    <div class="brand">
      <span class="brand-dot"></span>
      <span class="brand-name">Kinward Harbor Center</span>
      <span class="brand-tag">Building Stronger Families Together</span>
    </div>
    <div class="watermark" aria-hidden="true"></div>
    <div class="letter-foot">
      <p class="web">www.alderlanehub.org</p>
      <p class="contact-line">P: 973-555-0142 | F: 973-555-0143 | E: marisol.thackery@alderlanehub.org | 48 Alder Lane Morristown, NJ 07931</p>
    </div>
  </section>

  <section class="sheet env-back" aria-label="Envelope back">
    <svg width="521" height="156" viewBox="0 0 521 156" aria-hidden="true">
      <polyline points="0,0 180,96 341,96 521,0" fill="none" stroke="#d6d9de" stroke-width="1"/>
      <line x1="0" y1="156" x2="180" y2="96" stroke="#eceef1"/>
      <line x1="521" y1="156" x2="341" y2="96" stroke="#eceef1"/>
    </svg>
  </section>

  <section class="sheet env-front" aria-label="Envelope front">
    <div class="letter-foot">
      <p class="web">www.alderlanehub.org</p>
      <p class="contact-line">P: 973-555-0142 | F: 973-555-0143 | E: marisol.thackery@alderlanehub.org | 48 Alder Lane Morristown, NJ 07931</p>
    </div>
  </section>

</body>
</html>
```